Halvern Stationary Design

We're seeking a fresh and modern design for our stationery that captures the essence of our Real Estate brand. The current design, while functional, lacks visual appeal. We're looking for a more attractive and engaging design that showcases our professionalism and expertise in the real estate industry. I am attaching the current letter head and an image with a letter "P" as logo.

Target Market(s)

Real Estate Sales and Rentals

Industry/Entity Type

Real Estate

Requirements
Nice to have
• The owner seems to like the letter "P"

```html
<!DOCTYPE html>
<html lang="en">
<head>
<meta charset="utf-8">
<title>Halvern Property Solutions – Letterhead</title>
<link href="https://fonts.googleapis.com/css2?family=Poppins:ital,wght@0,400;0,500;0,600;0,700;1,400&display=swap" rel="stylesheet">
<style>
  :root {
    --backdrop: #8a8a8a;
    --paper: #f1f1f1;
    --navy: #434a61;
    --ink: #3c4460;
    --ink-soft: #5b6178;
    --watermark: #e2e2e6;
  }
  * { box-sizing: border-box; margin: 0; padding: 0; }
  html, body { width: 1200px; height: 800px; overflow: hidden; }
  body {
    background: var(--backdrop);
    font-family: "Poppins", sans-serif;
    color: var(--ink);
    position: relative;
  }
  .letterhead {
    position: absolute;
    left: 322px; top: 6px;
    width: 556px; height: 788px;
    background: var(--paper);
    overflow: hidden;
  }
  .letterhead__shapes { position: absolute; inset: 0; width: 100%; height: 100%; }
  .brand {
    position: absolute; top: 44px; left: 0; right: 0;
    display: flex; flex-direction: column; align-items: center; gap: 10px;
  }
  .brand__dot {
    width: 62px; height: 62px; border-radius: 50%;
    background: var(--navy);
  }
  .brand__name {
    font-size: 19px; font-weight: 600; color: var(--navy); letter-spacing: 0.1px;
  }
  .letter {
    position: absolute; top: 196px; left: 48px; right: 48px;
    font-size: 9.6px; line-height: 1.6; color: var(--ink);
  }
  .letter__greeting { font-weight: 700; font-size: 9.6px; margin-bottom: 10px; }
  .letter p + p { margin-top: 12px; }
  .letter__body p { text-align: justify; }
  .sign-off {
    position: absolute; left: 48px; top: 560px; width: 160px;
  }
  .sign-off__from { font-size: 10px; font-style: italic; color: var(--ink-soft); }
  .sign-off__name { font-size: 13px; font-weight: 700; color: var(--navy); line-height: 1.1; }
  .sign-off__role { font-size: 8.5px; font-style: italic; color: var(--ink-soft); }
  .sign-off__mark {
    margin-top: 8px; height: 26px; width: 150px;
    background: linear-gradient(90deg, rgba(67,74,97,0.10), rgba(67,74,97,0.02));
  }
  .sign-off__line { border-top: 1px solid var(--navy); margin-top: 2px; width: 150px; }
  .sign-off__label { font-size: 8.5px; margin-top: 4px; color: var(--ink); letter-spacing: 0.3px; }
  .contact {
    position: absolute; right: 30px; top: 590px;
    display: flex; flex-direction: column; align-items: flex-end; gap: 5px;
    font-size: 10.5px; font-weight: 500; color: var(--ink);
  }
  .contact__row { display: flex; align-items: center; gap: 8px; }
  .contact__icon { width: 11px; height: 11px; fill: var(--navy); }
  .contact__address { font-weight: 600; font-size: 10.5px; margin-top: 2px; }
  .tagline {
    position: absolute; right: 30px; top: 696px;
    font-size: 6.5px; color: var(--ink-soft); display: flex; gap: 8px;
  }
  .tagline span + span::before { content: "|"; margin-right: 8px; }
</style>
</head>
<body>
  <main class="letterhead">
    <svg class="letterhead__shapes" viewBox="0 0 556 788" aria-hidden="true">
      <path d="M300 0 H556 V128 C470 140 360 90 300 0 Z" fill="var(--navy)"/>
      <path d="M0 708 C90 660 210 690 262 788 H0 Z" fill="var(--navy)"/>
      <circle cx="300" cy="420" r="170" fill="var(--watermark)" opacity="0.55"/>
    </svg>

    <header class="brand">
      <span class="brand__dot"></span>
      <h1 class="brand__name">Halvern Property Solutions</h1>
    </header>

    <section class="letter">
      <p class="letter__greeting">DEAR SIR,</p>
      <div class="letter__body">
        <p>Lorem Ipsum is simply dummy text of the printing and typesetting industry. Lorem Ipsum has been the industry's standard dummy text ever since the 1500s, when an unknown printer took a galley of type and scrambled it to make a type specimen book. It has survived not only five centuries, but also the leap into electronic typesetting, remaining essentially unchanged.</p>
        <p>It was popularised in the 1960s with the release of Letraset sheets containing Lorem Ipsum passages, and more recently with desktop publishing software like Aldus PageMaker including versions of Lorem Ipsum.</p>
        <p>It is a long established fact that a reader will be distracted by the readable content of a page when looking at its layout. The point of using Lorem Ipsum is that it has a more-or-less normal distribution of letters, as opposed to using 'Content here, content here', making it look like readable English. Many desktop publishing packages and web page editors now use Lorem Ipsum as their default model text, and a search for 'lorem ipsum' will uncover many web sites still in their infancy. Various versions have evolved over the years, sometimes by accident, sometimes on purpose (injected humour and the like).</p>
      </div>
    </section>

    <section class="sign-off">
      <p class="sign-off__from">From,</p>
      <p class="sign-off__name">EDWIN CASTELL</p>
      <p class="sign-off__role">Creative Designer</p>
      <div class="sign-off__mark" role="img" aria-label="Handwritten signature"></div>
      <div class="sign-off__line"></div>
      <p class="sign-off__label">SIGNATURE</p>
    </section>

    <address class="contact">
      <span class="contact__row">555-410-2287
        <svg class="contact__icon" viewBox="0 0 24 24"><path d="M6.6 10.8a15.1 15.1 0 0 0 6.6 6.6l2.2-2.2a1 1 0 0 1 1-.25 11.4 11.4 0 0 0 3.6.57 1 1 0 0 1 1 1V20a1 1 0 0 1-1 1A17 17 0 0 1 3 4a1 1 0 0 1 1-1h3.5a1 1 0 0 1 1 1c0 1.25.2 2.45.57 3.57a1 1 0 0 1-.25 1z"/></svg>
      </span>
      <span class="contact__row">555-410-2290
        <svg class="contact__icon" viewBox="0 0 24 24"><path d="M6 3h12v5H6zM3 9h18v10h-3v2H6v-2H3zm5 6v4h8v-4z"/></svg>
      </span>
      <span class="contact__row">Halvernpropertysolutions.com
        <svg class="contact__icon" viewBox="0 0 24 24"><circle cx="12" cy="12" r="10"/><path d="M2 12h20M12 2c3 3 3 17 0 20M12 2c-3 3-3 17 0 20" stroke="#f1f1f1" stroke-width="1.5" fill="none"/></svg>
      </span>
      <span class="contact__row contact__address">48 Linden Crescent, Suite 2, Marlow Heights, MA 02199
        <svg class="contact__icon" viewBox="0 0 24 24"><path d="M12 2a7 7 0 0 0-7 7c0 5 7 13 7 13s7-8 7-13a7 7 0 0 0-7-7zm0 9.5A2.5 2.5 0 1 1 12 6.5a2.5 2.5 0 0 1 0 5z"/></svg>
      </span>
    </address>

    <p class="tagline">
      <span>Halvern Property Solutions</span>
      <span>The Rental Leader</span>
      <span>Serving Marlow's Real Estate Needs for 25+ Years</span>
    </p>
  </main>
</body>
</html>
```